Tide 4 Tide letterhead design and business card design for electrical company

I need a letterhead that can be used for my invoices and quote books along with emails sent to clients. I have a logo and the logo of Guild tradespeople I just need all my information placed nicely with a good flow.

Business Name: Tide 4 Tide Electrical
Name: Darren Kolvetis
Abn: 57804219362
Licence Number: 39417
Number: 0400683541

Thank you in advanced

Target Market(s)

Electrical Clients

Industry/Entity Type

Business

Contact Information for Business Card

Name: Darren Kolvetis
Abn: 57804219362
Licence Number: 39417
Number: 0400683541

Font styles to use
Sans Serif

Colors

Designer to choose colors to be used in the design.

Requirements
Must have
• Must have my logo, guild tradespeople logo even if its smaller and in the corner and all details
Nice to have
• Domestic Commercial Industrial stated on there somewhere

```html
<!DOCTYPE html>
<html lang="en">
<head>
<meta charset="utf-8">
<title>Tide 4 Tide Electrical – Business Card</title>
<link href="https://fonts.googleapis.com/css2?family=Open+Sans:wght@400;600;700&display=swap" rel="stylesheet">
<style>
  :root {
    --stage: #b4b4b4;
    --card-dark: #252425;
    --blue: #2a74c6;
    --blue-deep: #1a4f9e;
    --blue-light: #2f86cf;
    --white: #ffffff;
    --silver: #cfd2d6;
    --rule: #8d8d8d;
    --badge-green: #7cc242;
    --badge-navy: #143456;
  }
  * { margin: 0; padding: 0; box-sizing: border-box; }
  html, body {
    width: 1200px; height: 900px; overflow: hidden;
    background: var(--stage);
    font-family: "Open Sans", sans-serif;
  }
  .canvas { position: relative; width: 1200px; height: 900px; }

  .card { position: absolute; top: 170px; width: 346px; height: 560px; overflow: hidden; }

  .card-front { left: 259px; background: var(--card-dark); }
  .card-back {
    left: 631px;
    background: linear-gradient(135deg, var(--blue-deep) 0%, var(--blue-light) 50%, var(--blue-deep) 100%);
  }

  .brand { position: absolute; left: 0; right: 0; text-align: center; }
  .brand-front { top: 95px; }
  .brand-back { top: 252px; }
  .brand-name {
    font-weight: 700; font-size: 23px; line-height: 1.15;
    letter-spacing: 1px; text-transform: uppercase;
  }
  .brand-front .brand-name { color: var(--silver); }
  .brand-back .brand-name { color: var(--white); }
  .brand-dot {
    display: block; width: 16px; height: 16px; border-radius: 50%;
    margin: 0 auto 12px;
  }
  .brand-front .brand-dot { background: var(--blue); }
  .brand-back .brand-dot { background: var(--white); }

  .holder-name {
    position: absolute; top: 266px; left: 0; right: 0; text-align: center;
    color: var(--blue); font-size: 20px; font-weight: 400; letter-spacing: 0.3px;
  }
  .name-rule {
    position: absolute; top: 308px; left: 115px; width: 116px; height: 1px;
    background: var(--rule);
  }
  .details {
    position: absolute; top: 328px; left: 0; right: 0; text-align: center;
    color: var(--white); font-size: 14.5px; line-height: 24px;
  }
  .details .label { color: var(--blue); font-weight: 600; }
  .details .gap { height: 11px; }
  .details .web { color: var(--blue); font-weight: 600; line-height: 20px; }
  .details .email { line-height: 20px; }

  .member-band {
    position: absolute; left: 0; bottom: 0; width: 100%; height: 90px;
    background: linear-gradient(180deg, var(--blue-deep) 0%, var(--blue) 100%);
    display: flex; align-items: center; justify-content: center; gap: 6px;
  }
  .member-badge {
    width: 46px; height: 46px; border-radius: 4px; background: var(--badge-navy);
    border: 1px solid var(--badge-green);
  }
  .member-text {
    color: var(--white); font-weight: 700; font-size: 14.5px; line-height: 17px;
    text-transform: uppercase;
  }
</style>
</head>
<body>
<div class="canvas">

  <section class="card card-front" aria-label="Business card front">
    <div class="brand brand-front">
      <span class="brand-dot"></span>
      <div class="brand-name">Tide 4 Tide<br>Electrical</div>
    </div>

    <h1 class="holder-name">DARREN KOLVETIS</h1>
    <div class="name-rule"></div>

    <div class="details">
      <div><span class="label">ABN:</span> 57804219362</div>
      <div><span class="label">LICENCE NUMBER:</span> 39417</div>
      <div class="gap"></div>
      <div><span class="label">P:</span> 0400683541</div>
      <div class="email"><span class="label">E:</span> hello@tide4tide.com</div>
      <div class="web">www.tide4tide.com</div>
    </div>

    <div class="member-band">
      <span class="member-badge"></span>
      <div class="member-text">Guild<br>Tradespeople<br>Member</div>
    </div>
  </section>

  <section class="card card-back" aria-label="Business card back">
    <div class="brand brand-back">
      <span class="brand-dot"></span>
      <div class="brand-name">Tide 4 Tide<br>Electrical</div>
    </div>
  </section>

</div>
</body>
</html>
```